Construction Company Business Card

Business Card Design using new Logo

Contact Information for Business Card

include all company info and website

Requirements
Must have
• Wesley Corman - President
ph. 254-617-0382
Cedar Knoll, TX
wesley@ironmarkframing.com
www.ironmarkframing.com

```html
<!DOCTYPE html>
<html lang="en">
<head>
<meta charset="utf-8">
<title>Ironmark Framing – Business Card</title>
<link href="https://fonts.googleapis.com/css2?family=Roboto:wght@400;500;700&display=swap" rel="stylesheet">
<style>
  :root {
    --backdrop: #8f8f8f;
    --card: #231f20;
    --red: #c8202a;
    --light: #d9d9d9;
    --muted: #bdbdbd;
  }
  * { box-sizing: border-box; margin: 0; padding: 0; }
  html, body {
    width: 1200px; height: 960px; overflow: hidden;
    background: var(--backdrop);
    font-family: "Roboto", sans-serif;
  }
  .canvas { position: relative; width: 1200px; height: 960px; }
  .card {
    position: absolute; left: 272px; width: 655px; height: 374px;
    background: var(--card); overflow: hidden;
  }
  .card--front { top: 59px; }
  .card--back { top: 501px; }

  .map-area { position: absolute; }
  .card--front .map-area {
    left: 86px; top: 246px; width: 272px; height: 128px;
    background: linear-gradient(180deg, rgba(200,32,42,0.28), rgba(200,32,42,0.12));
  }
  .card--back .map-area {
    left: 35px; top: 0; width: 338px; height: 156px;
    background: linear-gradient(180deg, rgba(200,200,200,0.16), rgba(200,200,200,0.06));
  }

  .person { position: absolute; left: 82px; top: 160px; }
  .person__name { color: var(--red); font-weight: 700; font-size: 24px; letter-spacing: -0.5px; }
  .person__title { color: var(--light); font-size: 16px; margin-top: 4px; }

  .brand {
    display: flex; align-items: center; gap: 8px;
    color: var(--light); font-weight: 500; letter-spacing: 1px; text-transform: uppercase;
  }
  .brand__mark { width: 12px; height: 12px; background: var(--red); }
  .card--front .brand { position: absolute; left: 378px; top: 100px; font-size: 20px; }
  .card--back .brand {
    position: absolute; left: 0; right: 0; top: 190px; justify-content: center;
    font-size: 34px; gap: 14px;
  }
  .card--back .brand__mark { width: 18px; height: 18px; }

  .contact { position: absolute; left: 378px; top: 208px; list-style: none; color: var(--light); font-size: 17px; }
  .contact li { display: flex; align-items: flex-start; gap: 9px; line-height: 23px; }
  .contact li.contact__address { margin-bottom: 9px; }
  .contact svg { width: 14px; height: 14px; margin-top: 4px; flex: none; fill: var(--red); }

  .website { position: absolute; left: 0; right: 0; top: 298px; text-align: center; color: var(--light); font-size: 16px; }
</style>
</head>
<body>
<div class="canvas">
  <section class="card card--front">
    <div class="map-area" role="img" aria-label="Red outline of the Texas panhandle"></div>

    <div class="brand"><span class="brand__mark"></span>Ironmark Framing</div>

    <div class="person">
      <p class="person__name">Wesley Corman</p>
      <p class="person__title">President</p>
    </div>

    <ul class="contact">
      <li class="contact__address">
        <svg viewBox="0 0 14 14"><path d="M7 0a5 5 0 0 0-5 5c0 3.5 5 9 5 9s5-5.5 5-9a5 5 0 0 0-5-5zm0 7a2 2 0 1 1 0-4 2 2 0 0 1 0 4z"/></svg>
        <span>418 Juniper Bend<br>Cedar Knoll, TX 78655</span>
      </li>
      <li>
        <svg viewBox="0 0 14 14"><path d="M3 1l2.5 2.8-1.3 1.6a8 8 0 0 0 4.4 4.4l1.6-1.3L13 11l-1.6 2C6 13 1 8 1 2.6z"/></svg>
        <span>254-617-0382</span>
      </li>
      <li>
        <svg viewBox="0 0 14 14"><path d="M1 3h12v1L7 8 1 4zm0 2.3l6 4 6-4V11H1z"/></svg>
        <span>wesley@ironmarkframing.com</span>
      </li>
      <li>
        <svg viewBox="0 0 14 14"><circle cx="7" cy="7" r="6" fill="none" stroke="#c8202a" stroke-width="1.4"/><path d="M1 7h12M7 1v12" stroke="#c8202a" stroke-width="1.2"/></svg>
        <span>www.ironmarkframing.com</span>
      </li>
    </ul>
  </section>

  <section class="card card--back">
    <div class="map-area" role="img" aria-label="Light grey outline of southern Texas"></div>
    <div class="brand"><span class="brand__mark"></span>Ironmark Framing</div>
    <p class="website">www.ironmarkframing.com</p>
  </section>
</div>
</body>
</html>
```